TrueLane Collision Repair Web Site

Create a web site that will inform my potential customers about the services I provide. We are a Automotive Collision repair business that uses the latest state of the art equipment, computerized paint matching highly trained technicians, have over 30 years experience. We work with all all insurance programs. Our Moto is "Fixed Right, The First Time, Every Time". TrueLane, The intelligent choice in collision repair.

Target Market(s)

People that have been in a auto collision, needs windshield replaced, people that drive 10 year or newer cars

Industry/Entity Type

Automotive

Coding

Coded - Design and coding required

Number of Pages Required

4 page

Font styles to use
Sans Serif

Requirements
Must have
• Logo, Place for Phone number, I need to be able to put the code in so I can use a tracking phone number
• site needs to be mobile ready or adaptive
• May want to have a photo of a high end car
• here is a web site for example with the pages that I want
• https://www.brisvaleautobody.example/online-repair-estimate,
• https://www.brisvaleautobody.example/schedule-appointment
• https://www.brisvaleautobody.example/collision-repair/auto-body-repair
• https://www.brisvaleautobody.example/contact
Nice to have
• Be great if the Car in the log could have the front damaged then have it fix in a animation. Not sure if could be done here

```html
<!DOCTYPE html>
<html lang="en">
<head>
<meta charset="utf-8">
<title>TrueLane Collision Repair</title>
<link rel="stylesheet" href="https://fonts.googleapis.com/css2?family=Open+Sans:wght@400;600;700&family=Oswald:wght@400;500&display=swap">
<style>
:root{
  --navy:#0f1b3e;
  --navy-deep:#0b1633;
  --blue:#0d4fa6;
  --blue-bright:#1565c0;
  --green:#8dc63f;
  --green-dark:#6fa92a;
  --grey-bg:#e8e8e8;
  --text:#333;
  --orange:#f47a4a;
  --mint:#4fd1a5;
  --white:#fff;
}
*{box-sizing:border-box;margin:0;padding:0}
html,body{width:1200px;height:3462px;overflow:hidden}
body{font-family:"Open Sans",Arial,sans-serif;color:var(--text);background:var(--white);position:relative}
a{text-decoration:none}

/* header */
.site-header{position:absolute;left:0;top:0;width:1200px;height:132px;background:linear-gradient(#fff,#e4e4e4)}
.brand{position:absolute;left:70px;top:28px;color:var(--blue);font-family:"Open Sans",Arial,sans-serif;font-weight:700;line-height:1}
.brand .name{font-size:40px;letter-spacing:-.5px}
.brand .sub{display:block;font-size:17px;margin-top:4px;letter-spacing:1.5px;text-align:center}
.call{position:absolute;left:466px;top:40px;display:flex;align-items:center;gap:12px}
.call .ring{width:46px;height:46px;border-radius:50%;border:2px solid var(--navy);display:flex;align-items:center;justify-content:center}
.call small{display:block;font-size:13px;color:#333}
.call strong{display:block;font-family:"Oswald",sans-serif;font-weight:500;font-size:22px;color:var(--navy);line-height:1.1}
.head-btn{position:absolute;top:28px;height:82px;border:2px solid var(--blue);border-radius:8px;background:#fff;display:flex;align-items:center;gap:12px;padding-left:14px;color:var(--blue);font-family:"Oswald",sans-serif;font-size:22px;line-height:1.05;text-transform:uppercase}
.head-btn .dot{width:40px;height:40px;border-radius:50%;background:var(--blue);display:flex;align-items:center;justify-content:center;flex:none}
.btn-schedule{left:750px;width:191px}
.btn-estimate{left:953px;width:173px}

/* nav */
.main-nav{position:absolute;left:0;top:132px;width:1200px;height:48px;background:linear-gradient(var(--green),var(--green-dark));display:flex;justify-content:center;align-items:center}
.main-nav a{color:#fff;font-weight:700;font-size:13px;padding:0 14px;border-left:1px solid rgba(255,255,255,.45);line-height:16px}
.main-nav a:first-child{border-left:0}

/* hero */
.hero{position:absolute;left:0;top:180px;width:1200px;height:554px;background:linear-gradient(135deg,#2b2d31,#55585d 45%,#1d1f23)}
.hero-title{position:absolute;left:90px;top:180px;font-family:"Oswald",sans-serif;font-weight:400;font-size:58px;line-height:66px;color:#fff;text-transform:uppercase}
.hero-title span{display:table;background:var(--navy);padding:0 6px;margin-bottom:1px}
.slider-dots{position:absolute;left:1088px;top:230px;display:flex;flex-direction:column;gap:9px}
.slider-dots i{width:13px;height:13px;border-radius:50%;background:#b8bcc4;display:block}
.slider-dots i:first-child{background:var(--green)}

/* labels */
.tag{display:inline-block;background:var(--green);color:#fff;font-family:"Oswald",sans-serif;font-size:16px;padding:4px 12px;text-transform:uppercase}
.tag.blue{background:var(--blue)}

/* about */
.about{position:absolute;left:0;top:734px;width:1200px;height:588px}
.about .tag{position:absolute;left:74px;top:53px}
.about h2{position:absolute;left:74px;top:88px;width:520px;font-size:31px;line-height:36px;font-weight:700;color:#111}
.about .lead{position:absolute;left:74px;top:176px;width:510px;font-size:13px;line-height:20px;font-weight:700;color:#222}
.about .copy{position:absolute;left:74px;width:510px;font-size:13px;line-height:21px;color:#444}
.read-more{position:absolute;left:74px;top:491px;width:129px;height:42px;background:#111;color:#fff;font-family:"Oswald",sans-serif;font-size:15px;display:flex;align-items:center;justify-content:center;text-transform:uppercase}
.about .photo{position:absolute;left:614px;top:53px;width:512px;height:480px;background:linear-gradient(160deg,#4a6ea8,#2e3f5f 55%,#7b8796)}

/* services */
.services-head{position:absolute;left:0;top:1322px;width:1200px;height:127px;background:var(--blue)}
.services-head .tag{position:absolute;left:74px;top:34px}
.services-head h2{position:absolute;left:74px;top:66px;color:#fff;font-size:31px;font-weight:700}
.services-band{position:absolute;left:0;top:1449px;width:1200px;height:339px;background:var(--navy)}
.service-card{position:absolute;top:0;height:339px;background:linear-gradient(180deg,#24406f,#1a2d57 60%,#142449);color:#fff;text-align:center}
.service-card .icon{position:absolute;left:50%;top:46px;margin-left:-40px;width:80px;height:80px;border-radius:50%;border:2px solid var(--green);display:flex;align-items:center;justify-content:center}
.service-card h3{position:absolute;left:0;right:0;top:204px;font-family:"Oswald",sans-serif;font-weight:400;font-size:24px;text-transform:uppercase}
.service-card p{position:absolute;left:40px;right:40px;top:250px;font-size:13px;line-height:18px}

/* why */
.why{position:absolute;left:0;top:1788px;width:1200px;height:820px;background:var(--green);overflow:hidden}
.why .slant{position:absolute;left:0;top:0}
.why .tag{position:absolute;left:546px;top:60px;font-size:15px}
.why h2{position:absolute;left:0;right:0;top:96px;text-align:center;color:var(--navy);font-size:31px;line-height:38px;font-weight:700}
.why .photo{position:absolute;left:524px;top:206px;width:540px;height:554px;background:linear-gradient(150deg,#c8322e,#8c1d1d 50%,#3b3f46)}
.why-list{position:absolute;left:138px;top:261px;width:460px;height:443px;background:var(--navy);padding:34px 28px 0 24px;list-style:none}
.why-list li{display:flex;gap:14px;color:#fff;font-size:13px;line-height:22px;margin-bottom:22px}
.why-list svg{flex:none;margin-top:3px}

/* testimonials */
.testimonials{position:absolute;left:0;top:2608px;width:1200px;height:438px;background:var(--grey-bg)}
.testimonials .tag{position:absolute;left:74px;top:52px}
.testimonials h2{position:absolute;left:74px;top:86px;font-size:31px;font-weight:700;color:#222}
.quote{position:absolute;top:160px;width:340px}
.quote .avatar{position:absolute;left:0;top:12px;width:72px;height:72px;border-radius:50%;background:linear-gradient(#c9a98f,#8a6a55);border:3px solid #fff}
.quote p{position:absolute;left:88px;top:0;width:244px;font-size:13px;line-height:19px;color:#444}
.quote .who{position:absolute;left:88px;top:188px;font-size:13px;font-weight:700;color:#222}
.quote .who::before{content:"";position:absolute;left:0;top:-14px;width:30px;height:2px;background:var(--green)}

/* footer */
.site-footer{position:absolute;left:0;top:3046px;width:1200px;height:300px;background:var(--navy)}
.site-footer .brand{left:0;right:0;top:18px;text-align:center;color:var(--blue-bright)}
.contact-item{position:absolute;top:126px;display:flex;align-items:center;gap:18px;color:#fff;font-size:14px;line-height:20px}
.contact-item .ring{width:58px;height:58px;border-radius:50%;border:2px solid var(--blue-bright);display:flex;align-items:center;justify-content:center;flex:none}
.newsletter{position:absolute;left:245px;top:225px;display:flex;align-items:center;color:#fff;font-size:13px;font-weight:700}
.newsletter .field{width:318px;height:42px;background:#fff;margin-left:20px;color:#999;font-weight:400;padding-left:14px;display:flex;align-items:center}
.newsletter .subscribe{width:147px;height:42px;margin-left:12px;border:2px solid var(--blue-bright);color:var(--blue-bright);display:flex;align-items:center;justify-content:center;font-weight:700;font-size:13px}

.bottom-bar{position:absolute;left:0;top:3346px;width:1200px;height:116px;background:var(--navy-deep);border-top:1px solid #1d2b52}
.bottom-bar .copy{position:absolute;left:74px;top:24px;color:#fff;font-size:13px}
.social{position:absolute;left:74px;top:70px;display:flex;gap:10px}
.social i{width:30px;height:30px;border-radius:50%;border:1.5px solid #fff;display:block}
.foot-btn{position:absolute;top:19px;height:76px;border-radius:10px;display:flex;align-items:center;gap:12px;padding-left:18px;color:#fff;font-family:"Oswald",sans-serif;font-size:22px;line-height:1.05;text-transform:uppercase}
.foot-btn .dot{width:42px;height:42px;border-radius:50%;background:#fff;display:flex;align-items:center;justify-content:center;flex:none}
.foot-schedule{left:722px;width:213px;background:var(--orange)}
.foot-estimate{left:946px;width:180px;background:var(--mint)}
</style>
</head>
<body>

<header class="site-header">
  <div class="brand"><span class="name">TrueLane</span><span class="sub">Collision Repair</span></div>
  <div class="call">
    <span class="ring"><svg width="22" height="22" viewBox="0 0 24 24"><path d="M6.6 10.8a15 15 0 0 0 6.6 6.6l2.2-2.2c.3-.3.7-.4 1-.2 1.1.4 2.3.6 3.6.6.6 0 1 .4 1 1V20c0 .6-.4 1-1 1A17 17 0 0 1 3 4c0-.6.4-1 1-1h3.5c.6 0 1 .4 1 1 0 1.3.2 2.5.6 3.6.1.3 0 .7-.2 1z" fill="#0f1b3e"/></svg></span>
    <div><small>Call at now!</small><strong>(008) 5550 142 760</strong></div>
  </div>
  <a class="head-btn btn-schedule"><span class="dot"><svg width="20" height="20" viewBox="0 0 24 24"><rect x="3" y="5" width="18" height="16" rx="2" fill="none" stroke="#fff" stroke-width="2"/><path d="M3 10h18M8 3v4M16 3v4" stroke="#fff" stroke-width="2"/></svg></span><span>Schedule an<br>Appointment</span></a>
  <a class="head-btn btn-estimate"><span class="dot"><svg width="20" height="20" viewBox="0 0 24 24"><circle cx="12" cy="8" r="4" fill="#fff"/><path d="M4 21c0-4.4 3.6-7 8-7s8 2.6 8 7z" fill="#fff"/></svg></span><span>Online<br>Estimate</span></a>
</header>

<nav class="main-nav">
  <a>HOME</a><a>ABOUT US</a><a>NEED AN ESTIMATE?</a><a>IS YOUR CAR SAFE TO DRIVE?</a><a>SERVICES</a><a>FAQ</a><a>TESTIMONIALS</a><a>CONTACT US</a>
</nav>

<section class="hero" role="img" aria-label="Technician holding a diagnostic tablet inside a car interior">
  <h1 class="hero-title"><span>Fixed Right,</span><span>The First Time,</span><span>Every Time</span></h1>
  <div class="slider-dots"><i></i><i></i><i></i><i></i><i></i></div>
</section>

<section class="about">
  <span class="tag">About Us</span>
  <h2>TrueLane “The Intelligent Choice in Collision Repair”</h2>
  <p class="lead">Lorem ipsum dolor sit amet, consectetur adipiscing elit, sed do eiusmod tempor incididunt ut labore et dolore magna aliqua.</p>
  <p class="copy" style="top:240px">Lorem ipsum dolor sit amet, consectetur adipiscing elit, sed do eiusmod tempor incididunt ut labore et dolore magna aliqua. Ut enim ad minim veniam, quis nostrud exercitation ullamco laboris nisi ut aliquip ex ea commodo consequat. Duis aute irure dolor in reprehenderit in voluptate velit esse cillum dolore eu fugiat nulla pariatur. Excepteur sint occaecat cupidatat non proident, sunt in culpa qui officia deserunt mollit anim id est laborum.</p>
  <p class="copy" style="top:390px">laboris nisi ut aliquip ex ea commodo consequat. Duis aute irure dolor in reprehenderit in voluptate velit esse cillum dolore eu fugiat nulla pariatur. Excepteur sint occaecat cupidatat non proident, sunt in culpa qui officia deserunt mollit anim id est laborum.</p>
  <a class="read-more">Read More</a>
  <div class="photo" role="img" aria-label="Smiling mechanic in overalls standing in a repair shop with blue car lifts"></div>
</section>

<section class="services-head">
  <span class="tag">Services</span>
  <h2>We Provide Best Service</h2>
</section>
<section class="services-band">
  <article class="service-card" style="left:74px;width:348px" role="img" aria-label="Collision repair service over a dimmed workshop photo">
    <span class="icon"><svg width="40" height="40" viewBox="0 0 24 24"><path d="M6 4h8v6H6zM9 10v6M7 16h4v4H7zM14 6l5-2M14 8h6M14 10l5 2" fill="none" stroke="#fff" stroke-width="1.6"/></svg></span>
    <h3>Collision Repair</h3>
    <p>Lorem ipsum dolor sit amet, consectetur adipiscing elit.</p>
  </article>
  <article class="service-card" style="left:427px;width:344px" role="img" aria-label="Frame repair service over a dimmed workshop photo">
    <span class="icon"><svg width="40" height="40" viewBox="0 0 24 24"><path d="M4 14l2-6h12l2 6v5H4z" fill="none" stroke="#fff" stroke-width="1.6"/><circle cx="8" cy="15" r="1.3" fill="#fff"/><circle cx="16" cy="15" r="1.3" fill="#fff"/><path d="M6 19v2M18 19v2" stroke="#fff" stroke-width="1.6"/></svg></span>
    <h3>Frame Repair</h3>
    <p>Lorem ipsum dolor sit amet, consectetur adipiscing elit.</p>
  </article>
  <article class="service-card" style="left:778px;width:348px" role="img" aria-label="Wheel alignment service over a dimmed workshop photo">
    <span class="icon"><svg width="40" height="40" viewBox="0 0 24 24"><rect x="3" y="3" width="4" height="6" fill="#fff"/><rect x="17" y="3" width="4" height="6" fill="#fff"/><rect x="3" y="15" width="4" height="6" fill="#fff"/><rect x="17" y="15" width="4" height="6" fill="#fff"/><path d="M7 6h10M7 18h10M12 6v12" stroke="#fff" stroke-width="1.6"/></svg></span>
    <h3>Alignment</h3>
    <p>Lorem ipsum dolor sit amet, consectetur adipiscing elit.</p>
  </article>
</section>

<section class="why">
  <svg class="slant" width="1200" height="820" viewBox="0 0 1200 820"><polygon points="1200,400 1200,820 420,820" fill="#fff"/></svg>
  <span class="tag blue">TrueLane</span>
  <h2>Why is TrueLane the Intelligent<br>Choice in Collision Repair?</h2>
  <div class="photo" role="img" aria-label="Technicians in red uniforms working on an engine with a laptop"></div>
  <ul class="why-list">
    <li><svg width="16" height="16" viewBox="0 0 16 16"><circle cx="8" cy="8" r="7" fill="none" stroke="var(--green)" stroke-width="1.5"/><path d="M4.5 8.2l2.3 2.3 4.7-4.8" fill="none" stroke="var(--green)" stroke-width="1.6"/></svg>We ensure that latest OEM approved procedures are followed during each phase of the repair of your vehicle</li>
    <li><svg width="16" height="16" viewBox="0 0 16 16"><circle cx="8" cy="8" r="7" fill="none" stroke="var(--green)" stroke-width="1.5"/><path d="M4.5 8.2l2.3 2.3 4.7-4.8" fill="none" stroke="var(--green)" stroke-width="1.6"/></svg>We have the latest in computerized frame equipment</li>
    <li><svg width="16" height="16" viewBox="0 0 16 16"><circle cx="8" cy="8" r="7" fill="none" stroke="var(--green)" stroke-width="1.5"/><path d="M4.5 8.2l2.3 2.3 4.7-4.8" fill="none" stroke="var(--green)" stroke-width="1.6"/></svg>Our technicians are certified in structural repairs ensuring that your vehicle will be as safe for your family as it was the day it left the factory.</li>
    <li><svg width="16" height="16" viewBox="0 0 16 16"><circle cx="8" cy="8" r="7" fill="none" stroke="var(--green)" stroke-width="1.5"/><path d="M4.5 8.2l2.3 2.3 4.7-4.8" fill="none" stroke="var(--green)" stroke-width="1.6"/></svg>Our refinish equipment and trained painters will make sure your finish is back to factory finish maybe even better.</li>
    <li><svg width="16" height="16" viewBox="0 0 16 16"><circle cx="8" cy="8" r="7" fill="none" stroke="var(--green)" stroke-width="1.5"/><path d="M4.5 8.2l2.3 2.3 4.7-4.8" fill="none" stroke="var(--green)" stroke-width="1.6"/></svg>Each repair including paint and collision repair comes with a limited lifetime warranty as long as you own the vehicle.</li>
  </ul>
</section>

<section class="testimonials">
  <span class="tag">Testimonials</span>
  <h2>What Our Clients Say About Us</h2>
  <div class="quote" style="left:74px"><span class="avatar" role="img" aria-label="Client portrait"></span><p>Lorem ipsum dolor sit amet, consectetur adipiscing elit, sed do eiusmod tempor incididunt ut labore et dolore magna aliqua. Ut enim ad minim veniam, quis nostrud exercitation ullamco laboris nisi ut aliquip ex ea commodo consequat.</p><span class="who">Owen Hartley</span></div>
  <div class="quote" style="left:432px"><span class="avatar" role="img" aria-label="Client portrait"></span><p>Lorem ipsum dolor sit amet, consectetur adipiscing elit, sed do eiusmod tempor incididunt ut labore et dolore magna aliqua. Ut enim ad minim veniam, quis nostrud exercitation ullamco laboris nisi ut aliquip ex ea commodo consequat.</p><span class="who">Marco Bellini</span></div>
  <div class="quote" style="left:792px"><span class="avatar" role="img" aria-label="Client portrait"></span><p>Lorem ipsum dolor sit amet, consectetur adipiscing elit, sed do eiusmod tempor incididunt ut labore et dolore magna aliqua. Ut enim ad minim veniam, quis nostrud exercitation ullamco laboris nisi ut aliquip ex ea commodo consequat.</p><span class="who">Dean Whitaker</span></div>
</section>

<footer class="site-footer">
  <div class="brand"><span class="name">TrueLane</span><span class="sub">Collision Repair</span></div>
  <div class="contact-item" style="left:180px"><span class="ring"><svg width="24" height="24" viewBox="0 0 24 24"><path d="M6.6 10.8a15 15 0 0 0 6.6 6.6l2.2-2.2c.3-.3.7-.4 1-.2 1.1.4 2.3.6 3.6.6.6 0 1 .4 1 1V20c0 .6-.4 1-1 1A17 17 0 0 1 3 4c0-.6.4-1 1-1h3.5c.6 0 1 .4 1 1 0 1.3.2 2.5.6 3.6.1.3 0 .7-.2 1z" fill="#1565c0"/></svg></span>1-000-000-0000</div>
  <div class="contact-item" style="left:433px"><span class="ring"><svg width="24" height="24" viewBox="0 0 24 24"><path d="M12 2a7 7 0 0 0-7 7c0 5 7 13 7 13s7-8 7-13a7 7 0 0 0-7-7z" fill="#1565c0"/><circle cx="12" cy="9" r="2.6" fill="#0f1b3e"/></svg></span><span>Your Company LTD.<br>Street Name, 000000, City Name</span></div>
  <div class="contact-item" style="left:806px"><span class="ring"><svg width="24" height="24" viewBox="0 0 24 24"><rect x="3" y="5" width="18" height="14" rx="1.5" fill="#1565c0"/><path d="M3.5 6l8.5 7 8.5-7" fill="none" stroke="#0f1b3e" stroke-width="1.6"/></svg></span>info@truelanerepair.example</div>
  <div class="newsletter">STAY INFORMED OUR UPDATES<span class="field">Enter your e-mail address</span><span class="subscribe">SUBSCRIBE</span></div>
</footer>

<div class="bottom-bar">
  <p class="copy">© 2016 TrueLane Collision Repair. All Rights Reserved</p>
  <div class="social"><i></i><i></i></div>
  <a class="foot-btn foot-schedule"><span class="dot"><svg width="22" height="22" viewBox="0 0 24 24"><rect x="3" y="5" width="18" height="16" rx="2" fill="none" stroke="#0f1b3e" stroke-width="2"/><path d="M3 10h18M8 3v4M16 3v4" stroke="#0f1b3e" stroke-width="2"/></svg></span><span>Schedule an<br>Appointment</span></a>
  <a class="foot-btn foot-estimate"><span class="dot"><svg width="22" height="22" viewBox="0 0 24 24"><circle cx="12" cy="8" r="4" fill="#0f1b3e"/><path d="M4 21c0-4.4 3.6-7 8-7s8 2.6 8 7z" fill="#0f1b3e"/></svg></span><span>Online<br>Estimate</span></a>
</div>

</body>
</html>
```